Larkspur Stillness

Logo picture and I want it to say

yoga. meditation. sound healing

small sweet classes

Larkspur-stillness.com

2740 West Hollander Ave Suite K
Santa Barbara ca 93108

```html
<!DOCTYPE html>
<html lang="en">
<head>
<meta charset="UTF-8">
<title>Larkspur Stillness – Meditation Classes Flyer</title>
<link rel="stylesheet" href="https://fonts.googleapis.com/css2?family=Montserrat:wght@400;500;600;700&family=Source+Sans+3:wght@600&family=Allura&display=swap">
<style>
  :root {
    --canvas-bg: #e8e5e1;
    --paper: #ffffff;
    --ink: #2b2b2d;
    --ink-soft: #3c3c3e;
    --swoosh: #58585b;
    --badge: #5f5f62;
    --badge-ring: #bdbdbf;
    --frame: #c9c9cb;
    --bar: #cfcfd0;
    --bar-text: #4a4a4c;
    --photo-light: #f7f8f9;
    --photo-mid: #e4eaee;
    --photo-aqua: #8fd0dd;
    --photo-peach: #f2b8a4;
  }
  * { margin: 0; padding: 0; box-sizing: border-box; }
  html, body { width: 1200px; height: 1200px; overflow: hidden; }
  body { background: var(--canvas-bg); position: relative; font-family: "Montserrat", sans-serif; color: var(--ink); }

  .flyer {
    position: absolute; left: 150px; top: 20px;
    width: 900px; height: 1160px;
    background: var(--paper);
    overflow: hidden;
  }
  .flyer-art { position: absolute; left: 0; top: 0; width: 900px; height: 700px; }
  .flyer-frame {
    position: absolute; left: 27px; top: 26px; width: 847px; height: 1104px;
    border: 2px solid var(--frame);
    pointer-events: none;
  }

  .brand-mark {
    position: absolute; left: 49px; top: 48px;
    width: 134px; height: 134px;
    border: 2px solid var(--ink-soft); border-radius: 50%;
    display: flex; flex-direction: column; align-items: center; justify-content: center;
    font-family: "Montserrat", sans-serif; font-weight: 500; color: var(--ink-soft);
    font-size: 14px; line-height: 1.25; text-align: center; letter-spacing: 0.5px;
  }

  .headline { position: absolute; left: 44px; top: 206px; }
  .headline-kicker {
    font-weight: 700; font-size: 55px; line-height: 54px; letter-spacing: 1px;
    color: var(--ink);
  }
  .headline-sub { font-weight: 600; font-size: 54px; line-height: 54px; color: var(--ink); }
  .headline-place {
    font-family: "Allura", cursive; font-size: 122px; line-height: 110px;
    color: var(--ink-soft); margin-left: 2px;
  }

  .price-badge {
    position: absolute; left: 66px; top: 495px;
    width: 194px; height: 194px; border-radius: 50%;
    background: var(--badge-ring);
    display: flex; align-items: center; justify-content: center;
  }
  .price-badge-inner {
    width: 178px; height: 178px; border-radius: 50%;
    background: var(--badge); color: #fff; margin-left: 10px; margin-top: 6px;
    display: flex; flex-direction: column; align-items: center; justify-content: center;
    text-align: center;
  }
  .price-label { font-size: 14px; font-weight: 500; letter-spacing: 1px; }
  .price-amount { font-size: 36px; font-weight: 600; line-height: 44px; }
  .price-unit { font-size: 20px; font-weight: 500; line-height: 22px; }

  .intro-question {
    position: absolute; left: 60px; width: 780px; top: 736px;
    font-family: "Source Sans 3", sans-serif; font-weight: 600;
    font-size: 22px; line-height: 28px; text-align: center; color: var(--ink-soft);
  }
  .divider { position: absolute; left: 352px; top: 839px; width: 197px; height: 2px; background: var(--ink-soft); }

  .body-copy {
    position: absolute; left: 75px; width: 750px; top: 866px;
    font-size: 13.6px; line-height: 17.5px; text-align: center; color: var(--ink);
  }
  .body-copy p + p { margin-top: 17px; }

  .service-bar {
    position: absolute; left: 146px; top: 1017px; width: 623px; height: 41px;
    background: var(--bar);
    display: flex; align-items: center; justify-content: space-around;
    font-size: 16px; font-weight: 500; letter-spacing: 3px; color: var(--bar-text);
  }
  .service-bar .sep { width: 2px; height: 22px; background: #fff; }

  .web-address {
    position: absolute; left: 0; width: 900px; top: 1087px;
    text-align: center; font-size: 17px; letter-spacing: 2.5px; color: var(--ink);
  }
</style>
</head>
<body>
  <main class="flyer">
    <svg class="flyer-art" viewBox="0 0 900 700" xmlns="http://www.w3.org/2000/svg">
      <defs>
        <linearGradient id="photoBase" x1="0" y1="0" x2="1" y2="0">
          <stop offset="0" stop-color="var(--photo-light)"/>
          <stop offset="0.45" stop-color="#f4f5f6"/>
          <stop offset="0.7" stop-color="var(--photo-mid)"/>
          <stop offset="1" stop-color="#dfe9ec"/>
        </linearGradient>
        <radialGradient id="photoAqua" cx="0.88" cy="0.7" r="0.35">
          <stop offset="0" stop-color="var(--photo-aqua)" stop-opacity="0.85"/>
          <stop offset="1" stop-color="var(--photo-aqua)" stop-opacity="0"/>
        </radialGradient>
        <radialGradient id="photoPeach" cx="0.68" cy="0.55" r="0.2">
          <stop offset="0" stop-color="var(--photo-peach)" stop-opacity="0.7"/>
          <stop offset="1" stop-color="var(--photo-peach)" stop-opacity="0"/>
        </radialGradient>
        <linearGradient id="photoFloor" x1="0" y1="0" x2="0" y2="1">
          <stop offset="0.6" stop-color="#8d9196" stop-opacity="0"/>
          <stop offset="1" stop-color="#8d9196" stop-opacity="0.35"/>
        </linearGradient>
      </defs>
      <g role="img" aria-label="Photo of women meditating cross-legged on yoga mats in a bright studio">
        <path d="M0,0 H900 V566 C760,640 640,668 520,666 C340,662 170,600 0,520 Z" fill="url(#photoBase)"/>
        <path d="M0,0 H900 V566 C760,640 640,668 520,666 C340,662 170,600 0,520 Z" fill="url(#photoPeach)"/>
        <path d="M0,0 H900 V566 C760,640 640,668 520,666 C340,662 170,600 0,520 Z" fill="url(#photoAqua)"/>
        <path d="M0,0 H900 V566 C760,640 640,668 520,666 C340,662 170,600 0,520 Z" fill="url(#photoFloor)"/>
      </g>
      <path class="swoosh" d="M0,440 C110,560 290,684 520,686 C680,688 820,628 900,568 C790,640 650,668 520,666 C330,662 160,596 0,520 Z" fill="var(--swoosh)"/>
    </svg>

    <div class="flyer-frame"></div>

    <div class="brand-mark">Larkspur<br>Stillness</div>

    <h1 class="headline">
      <div class="headline-kicker">MEDITATION</div>
      <div class="headline-sub">clases in</div>
      <div class="headline-place">Larkspur</div>
    </h1>

    <div class="price-badge">
      <div class="price-badge-inner">
        <span class="price-label">CLASSES ARE</span>
        <span class="price-amount">$20.00</span>
        <span class="price-unit">/class</span>
      </div>
    </div>

    <p class="intro-question">Do you want to have more clarity and focus? Or,<br>do you want to be more productive and balanced? Or, do you just want to<br>feel more connected to yourself?</p>
    <div class="divider"></div>

    <div class="body-copy">
      <p>Meditation can lower blood pressure, reduce anxiety and alleviate digestive issues.&nbsp; Meditation has been clinically proven to reduce stress, depression and can even help cure numerous types of chronic pain and illness.</p>
      <p>Larkspur Stillness classes are designed to be 35 to 45 minutes. Each class will begin with a brief discussion and some tips to help for a successful meditation. Part of meditation is not to have a worry. To support this balance, all classes begin and end on time.</p>
    </div>

    <nav class="service-bar">
      <span>YOGA</span><span class="sep"></span><span>MEDITATION</span><span class="sep"></span><span>SOUND HEALING</span>
    </nav>

    <p class="web-address">www.larkspur-stillness.com</p>
  </main>
</body>
</html>
```